Icon-Design für App
Zielgruppe
quobarin.com is an app for more social closeness: You can scan people around you (50m) and give quobarins (nobody can see your likes unless you like each other). It's a kind of the opposite of Flurma: Meet first live in a bar, during shopping at the bus-station.... and use the app just as an 'ice-breaker'. Therefore the scanner of quobarin.com is very accurate (50m) and realtime....which is so far unique. We got more than 1000 Users within the first weeks after launch...and it's time to style the app as many people said it looks terrible.... Quobarin is available on appvelo depot or just as a web app in every browser over www.quobarin.com.
Aufgabenstellung
we got many feedbacks that the app-function is great but the design looks terrible. Can you change this? If you tested the app (www.quobarin.com) and once you understood the idea: feel free to follow your feelings when re-designing! We are open to all changes. I actually would like to keep the main logo, the 'shy smiling heart with the hand in front of mouth'...but if you have a better Idea...just do it!

```html
<!DOCTYPE html>
<html lang="en">
<head>
<meta charset="utf-8">
<title>Quobarin – Nearby list</title>
<link rel="stylesheet" href="https://fonts.googleapis.com/css2?family=Roboto:wght@400;500;700&family=Roboto+Mono:wght@700&display=swap">
<style>
  :root{
    --page:#f2f2f2;
    --orange-top:#fb9a00;
    --orange-bottom:#f05a06;
    --accent:#f05a0a;
    --badge-a:#f26a3a;
    --badge-b:#e8452c;
    --yellow:#f8b800;
    --grey-icon:#cfcfcf;
    --row-alt:#d6d6d6;
    --white:#ffffff;
    --ink:#333333;
    --indicator:#c8c8c8;
  }
  *{box-sizing:border-box;margin:0;padding:0}
  html,body{width:1200px;height:960px;overflow:hidden;background:var(--page);font-family:"Roboto",sans-serif}
  .screen{position:absolute;left:385px;top:20px;width:430px;height:920px;border-radius:46px;overflow:hidden;background:var(--white);box-shadow:0 6px 30px rgba(0,0,0,.08)}
  .header{position:absolute;left:0;top:0;width:100%;height:266px;background:linear-gradient(180deg,var(--orange-top),var(--orange-bottom))}
  .status-time{position:absolute;left:40px;top:20px;font-size:12px;font-weight:500;color:#222}
  .status-icons{position:absolute;right:26px;top:20px}
  .icon-logout{position:absolute;left:22px;top:78px}
  .icon-help{position:absolute;right:22px;top:79px}
  .profile-photo{position:absolute;left:146px;top:59px;width:139px;height:139px;border-radius:50%;border:3px solid var(--white);background:radial-gradient(circle at 50% 45%,#c79a7c 0 30%,#6f8fe8 31% 100%)}
  .brand-name{position:absolute;left:0;top:212px;width:100%;text-align:center;color:var(--white);font-size:32px;font-weight:400;letter-spacing:5px}
  .nearby-list{position:absolute;left:0;top:266px;width:100%;height:519px;overflow:hidden}
  .user-row{position:relative;height:91px;background:var(--white)}
  .user-row:nth-child(even){background:var(--row-alt)}
  .user-photo{position:absolute;left:22px;top:10px;width:72px;height:72px;border-radius:50%}
  .distance-badge{position:absolute;left:100px;top:29px;height:33px;padding:0 8px 0 11px;border-radius:17px;background:linear-gradient(90deg,var(--badge-a),var(--badge-b));color:var(--white);font-size:11px;font-weight:500;line-height:33px}
  .distance-badge::before{content:"";position:absolute;left:-5px;bottom:4px;border-top:8px solid transparent;border-right:10px solid var(--badge-a)}
  .chat-icon{position:absolute;left:268px;top:22px}
  .like-icon{position:absolute;left:351px;top:19px}
  .like-pending{position:absolute;left:357px;top:22px;width:46px;height:46px;border-radius:50%;border:3px solid var(--yellow)}
  .like-pending.is-grey{border-color:var(--grey-icon);background:var(--white)}
  .bottom-nav{position:absolute;left:0;top:785px;width:100%;height:135px;background:var(--white)}
  .nav-item{position:absolute;top:30px;width:110px;text-align:center;font-size:16px;font-weight:500;color:var(--ink)}
  .nav-friends{left:17px}
  .nav-community{left:293px}
  .nav-item svg{display:block;margin:0 auto 4px}
  .friends-count{position:absolute;left:62px;top:-6px;width:22px;height:22px;border-radius:50%;background:var(--accent);color:var(--white);font-size:13px;line-height:22px;font-weight:500}
  .scan-button{position:absolute;left:148px;top:-32px;width:122px;height:122px;border-radius:50%;background:#f27a2e;box-shadow:0 4px 10px rgba(0,0,0,.15);display:flex;align-items:center;justify-content:center}
  .scan-button-core{width:88px;height:88px;border-radius:50%;background:var(--accent);display:flex;align-items:center;justify-content:center}
  .scan-label{position:absolute;left:0;top:89px;width:100%;text-align:center;font-family:"Roboto Mono",monospace;font-weight:700;font-size:16px;letter-spacing:2px;color:var(--accent)}
  .home-indicator{position:absolute;left:153px;top:120px;width:120px;height:4px;border-radius:2px;background:var(--indicator)}
</style>
</head>
<body>
<svg width="0" height="0" style="position:absolute">
  <defs>
    <symbol id="heart" viewBox="0 0 52 46"><path d="M26 45 C12 34 1 26 1 14 A12.5 12.5 0 0 1 26 8 A12.5 12.5 0 0 1 51 14 C51 26 40 34 26 45Z"/></symbol>
    <symbol id="chat" viewBox="0 0 48 44"><path d="M8 5h36a3 3 0 0 1 3 3v20a3 3 0 0 1-3 3h-3v7l-6-7h-1V12a3 3 0 0 0-3-3H8z" opacity=".75"/><path d="M3 9h30a3 3 0 0 1 3 3v20a3 3 0 0 1-3 3H18l-7 7v-7H3a3 3 0 0 1-3-3V12a3 3 0 0 1 3-3z"/><path d="M6 16h20M6 21h24M6 26h16" stroke="#fff" stroke-width="2"/></symbol>
  </defs>
</svg>

<main class="screen">
  <header class="header">
    <span class="status-time">9:41</span>
    <svg class="status-icons" width="52" height="12" viewBox="0 0 52 12"><rect x="0" y="8" width="3" height="4" fill="#222"/><rect x="4.5" y="6" width="3" height="6" fill="#222"/><rect x="9" y="3" width="3" height="9" fill="#222"/><rect x="13.5" y="0" width="3" height="12" fill="#222" opacity=".4"/><path d="M22 5a9 9 0 0 1 12 0M24.5 7.5a5 5 0 0 1 7 0" stroke="#222" stroke-width="1.6" fill="none"/><circle cx="28" cy="10" r="1.4" fill="#222"/><rect x="38" y="2" width="13" height="8" rx="2" fill="#222"/></svg>
    <svg class="icon-logout" width="36" height="36" viewBox="0 0 36 36" fill="none" stroke="#fff" stroke-width="2"><path d="M16 4H5v28h11"/><path d="M33 18H13M20 11l-7 7 7 7"/></svg>
    <svg class="icon-help" width="32" height="32" viewBox="0 0 32 32" fill="none" stroke="#fff" stroke-width="2"><circle cx="16" cy="16" r="14"/><path d="M11.5 12.5a4.5 4.5 0 1 1 6 4.2c-1 .5-1.5 1.3-1.5 2.5v1.3"/><circle cx="16" cy="24" r="1" fill="#fff"/></svg>
    <div class="profile-photo" role="img" aria-label="Profile photo of the signed-in user"></div>
    <h1 class="brand-name">Quobarin</h1>
  </header>

  <section class="nearby-list">
    <div class="user-row">
      <div class="user-photo" role="img" aria-label="Photo of a nearby user" style="background:#8a7d55"></div>
      <span class="distance-badge">New 50m</span>
      <svg class="chat-icon" width="48" height="44" fill="var(--grey-icon)"><use href="#chat"/></svg>
      <span class="like-pending" role="img" aria-label="Shy like, waiting"></span>
    </div>
    <div class="user-row">
      <div class="user-photo" role="img" aria-label="Photo of a nearby user" style="background:#1f2f66"></div>
      <span class="distance-badge">New 50m</span>
      <svg class="chat-icon" width="48" height="44" fill="var(--yellow)"><use href="#chat"/></svg>
      <svg class="like-icon" width="55" height="50" fill="var(--accent)"><use href="#heart"/></svg>
    </div>
    <div class="user-row">
      <div class="user-photo" role="img" aria-label="Photo of a nearby user" style="background:#3a3a3a"></div>
      <span class="distance-badge">New 50m</span>
      <svg class="chat-icon" width="48" height="44" viewBox="0 0 48 44"><path d="M8 5h36a3 3 0 0 1 3 3v20a3 3 0 0 1-3 3h-3v7l-6-7h-1V12a3 3 0 0 0-3-3H8z" fill="var(--accent)" opacity=".75"/><path d="M3 9h30a3 3 0 0 1 3 3v20a3 3 0 0 1-3 3H18l-7 7v-7H3a3 3 0 0 1-3-3V12a3 3 0 0 1 3-3z" fill="var(--accent)"/><text x="18" y="27" text-anchor="middle" font-family="Roboto,sans-serif" font-size="13" font-weight="700" fill="#fff">NEW</text></svg>
      <svg class="like-icon" width="55" height="50" fill="var(--accent)"><use href="#heart"/></svg>
    </div>
    <div class="user-row">
      <div class="user-photo" role="img" aria-label="Photo of a nearby user" style="background:#7a4a35"></div>
      <span class="distance-badge">New 50m</span>
      <svg class="chat-icon" width="48" height="44" fill="var(--yellow)"><use href="#chat"/></svg>
      <span class="like-pending is-grey" role="img" aria-label="Shy like, not sent"></span>
    </div>
    <div class="user-row">
      <div class="user-photo" role="img" aria-label="Photo of a nearby user" style="background:#6b5a58"></div>
      <span class="distance-badge">New 50m</span>
      <svg class="chat-icon" width="48" height="44" fill="var(--grey-icon)"><use href="#chat"/></svg>
      <span class="like-pending" role="img" aria-label="Shy like, waiting"></span>
    </div>
    <div class="user-row">
      <div class="user-photo" role="img" aria-label="Photo of a nearby user" style="background:#3b4a66"></div>
      <span class="distance-badge">New 50m</span>
      <svg class="chat-icon" width="48" height="44" fill="var(--yellow)"><use href="#chat"/></svg>
      <svg class="like-icon" width="55" height="50" fill="var(--accent)"><use href="#heart"/></svg>
    </div>
  </section>

  <nav class="bottom-nav">
    <div class="nav-item nav-friends">
      <svg width="44" height="34" viewBox="0 0 44 34" fill="#333"><circle cx="13" cy="9" r="6"/><path d="M1 30c0-8 5-13 12-13s12 5 12 13z"/><circle cx="27" cy="11" r="5"/><path d="M24 30c0-6 2-10 5-12 6 0 11 5 11 12z"/></svg>
      Friends
      <span class="friends-count">1</span>
    </div>
    <div class="scan-button">
      <div class="scan-button-core">
        <svg width="50" height="44" fill="#fff"><use href="#heart"/></svg>
      </div>
    </div>
    <span class="scan-label">Scan 50 m</span>
    <div class="nav-item nav-community">
      <svg width="36" height="34" viewBox="0 0 36 36"><circle cx="18" cy="18" r="16" fill="#333"/><path d="M8 9c4 1 6 4 5 7s-4 3-3 7 3 5 3 9C7 29 3 22 4 16M20 3c2 3 6 3 9 6s1 6 4 9M22 20c3 1 5 4 4 8s-3 4-5 5c-1-4-3-6-2-10z" fill="#fff"/></svg>
      Community
    </div>
    <span class="home-indicator"></span>
  </nav>
</main>
</body>
</html>
```